VistaLume webpage - Design only no coding required

Please refer to "web content" uploaded 23rd Sep for content

We are a digital signage company based in Jakarta, Indonesia.

Our core business is placement of LCD Tv's in waiting rooms of various hospitals in Indonesia which plays educational videos regarding various health topics (prescription/ethical medicines), OTC drugs TVC and other FMCG and ads.

Our client portfolio consists of the worlds biggest and well known Pharmaceutical companies and also local pharmaceutical companies.

Other parts of our business are as follows:
- Patient symposiums
- Booths for product activation
- Queuing systems that we have developed in house that use an android tablet and connect to our TV's
- Branding. eg. Lift doors, banners (static signage)
- Hospital management software. Specially developed software that comes in a generic format and needs to be customized to suit each hospital. It manages everything for phone/web booking, queues, registration, patient records, doctors schedules, referrals, pharmacy and inventory and checkout/payments.

We are after a website redesign that is visually attractive and modern as we also deal with many advertising agencies.

Our logo is orange and black, however the black & white can be reversed if necessary.

Pages will need to be available in English & Bahasa Indonesia language formats.

I am happy to answer any questions asap, i can be contacted at info@vistalume.example.id

current site (www.vistalume.example.id)

Target Market(s)

Mainly our business is B2B dealing with advertising clients either directly or through ad agencies.

The other aspect of our target market is hospitals where we place our screens.

There is (but not largely) and consumer audience.

In summary:
We have the following target markets:
1. Advertisers/ad agencies
2. Hospitals that wish to use our business model to display content to their patients 3. We are in a developing country however most of our viewers and clients are from a high demographic profile

Industry/Entity Type

Pharmaceutical

Requirements
Must have
• We will require duplicates of the pages in English & Bahasa Indonesia

I would like the initial designs with a focus on being clean yet bold and emphasis on typography.

The following pages will be required (but not limited to) to qualify for the prize:

-Home

- About Us

- Services
(sub pages)
=Digital Signage
=Video Content Production
=Hospital Branding
=Event Management
=Seminar
=Queue System
=Hospital Management Software

-Why Choose Us?

- Contact Us

- Clients & Partners

- Gallery

Based on the "Nice to haves" site examples we do not necessarily require pictures of our LCD's/content on the main page(s) and would be happy to purchase required stock photos if needed/agreed.

We definitely want a modern feel and do not wish to overload with too much info on the main page.

(Please note the text in the attached file will most likely be changed once we have a design concept, probably less text)

Webpages we like:
http://www.brinklanternstudio.example/
http://quillharbor.example

Nice to have
• This is some of the international players which we want our site to look like:
www.pardelsign.example.au
http://www.morvexpanel.example.uk/
www.tallowgrid.example/

Should not have
• We prefer not to have old outdated fonts and a website that resembles anything like the current one, we are after a modern and professional feel.
These are some of our relative competitors of which we DO NOT want our website looking like but as a reference:
http://curabyte-global.example/index.html
http://zrk.example.id/

```html
<!DOCTYPE html>
<html lang="en">
<head>
<meta charset="utf-8">
<title>VistaLume — Digital Signage Network</title>
<link rel="stylesheet" href="https://fonts.googleapis.com/css2?family=Oswald:wght@400;500&family=Open+Sans:wght@400;700;800&family=Tinos&display=swap">
<style>
:root{
  --orange:#e8641b;
  --orange-dark:#c9520f;
  --black:#0c0c0c;
  --ink:#1d1d1d;
  --body:#555;
  --white:#fff;
  --mist:#eef0f1;
  --sky-1:#9fc3de;
  --sky-2:#e6eef5;
  --card:rgba(255,255,255,.78);
  --grey:#8b8b8b;
}
*{margin:0;padding:0;box-sizing:border-box}
html,body{width:1200px;height:2812px;overflow:hidden;background:var(--white)}
body{position:relative;font-family:'Open Sans',sans-serif;color:var(--ink)}
.abs{position:absolute}

/* header */
.site-header{position:absolute;left:0;top:0;width:1200px;height:89px;background:var(--black)}
.brand{position:absolute;left:136px;top:22px;display:flex;align-items:center;gap:12px}
.brand-mark{width:40px;height:40px;background:var(--orange)}
.brand-name{font-family:'Open Sans',sans-serif;font-weight:700;font-size:34px;color:var(--white);letter-spacing:-.5px}
.main-nav{position:absolute;left:448px;top:30px;display:flex;gap:14px}
.main-nav a{font-family:'Oswald',sans-serif;font-size:18px;color:var(--white);text-decoration:none;text-transform:uppercase;letter-spacing:-.3px;padding-bottom:5px;white-space:nowrap}
.main-nav a.is-active{border-bottom:3px solid var(--orange)}

/* hero */
.hero{position:absolute;left:0;top:89px;width:1200px;height:469px;background:linear-gradient(90deg,#dcdcdc 0%,#f1f1f1 35%,#e7e2dc 60%,#d9d4cf 100%)}
.hero-floor{position:absolute;left:0;bottom:0;width:1200px;height:150px;background:linear-gradient(180deg,#c9b79e,#b69c7c)}
.hero-rule{position:absolute;left:0;top:556px;width:1200px;height:4px;background:var(--orange)}
.hero-caption{position:absolute;left:136px;top:387px;width:540px;height:122px;background:rgba(255,255,255,.85);padding:17px 0 0 26px}
.hero-caption h1{font-family:'Open Sans',sans-serif;font-weight:800;font-size:25px;line-height:30px;color:var(--ink);text-transform:uppercase;white-space:nowrap;letter-spacing:.2px}
.hero-caption h1 em{font-style:normal;color:var(--orange)}

.section-title{font-family:'Oswald',sans-serif;font-weight:400;font-size:33px;color:var(--ink);text-transform:uppercase;letter-spacing:-.3px;white-space:nowrap}
.serif-copy{font-family:'Tinos',serif;font-size:16px;line-height:27px;color:var(--body)}

/* welcome */
.welcome-title{left:136px;top:622px}
.welcome-copy{left:136px;top:680px;width:480px}
.video-frame{position:absolute;left:663px;top:663px;width:410px;height:235px;background:#111;border-radius:6px;overflow:hidden;box-shadow:0 10px 18px rgba(0,0,0,.25)}
.video-still{position:absolute;inset:0;background:linear-gradient(135deg,#4b5560,#2a2f34 60%,#151719)}
.video-bar{position:absolute;left:0;bottom:0;width:100%;height:30px;background:rgba(0,0,0,.8)}
.video-progress{position:absolute;left:58px;bottom:12px;width:230px;height:5px;background:#55606a}
.video-progress span{display:block;width:40%;height:100%;background:#2c8ad6}

/* services */
.services{position:absolute;left:0;top:968px;width:1200px;height:666px;background:linear-gradient(180deg,var(--sky-1) 0%,var(--sky-2) 45%,#b9cbd8 100%)}
.services-title{position:absolute;left:0;top:54px;width:1200px;text-align:center;font-size:31px}
.service-card{position:absolute;width:277px;height:128px;background:var(--card);border-radius:4px;padding:18px 0 0 45px}
.service-card h3{font-family:'Open Sans',sans-serif;font-weight:400;font-size:19px;color:var(--ink);margin-bottom:8px;white-space:nowrap}
.service-card p{font-family:'Tinos',serif;font-size:14px;line-height:19px;color:#444;width:205px}
.service-card.is-active{background:var(--black)}
.service-card.is-active h3{color:var(--orange)}
.service-card.is-active p{color:#ddd}
.service-icon{position:absolute;left:-14px;top:-26px;width:54px;height:54px}

/* why */
.why-photo{position:absolute;left:164px;top:1711px;width:422px;height:293px;background:linear-gradient(135deg,#dfe4e8,#f7f7f7 55%,#cfd6dc)}
.why-title{left:652px;top:1733px}
.why-copy{left:652px;top:1795px;width:418px}

/* newsletter */
.newsletter{position:absolute;left:0;top:2051px;width:1200px;height:492px;background:#ececec}
.newsletter-title{position:absolute;left:0;top:56px;width:1200px;text-align:center;font-size:31px}
.newsletter-sub{position:absolute;left:0;top:116px;width:1200px;text-align:center}
.email-field{position:absolute;left:363px;top:166px;width:279px;height:47px;background:var(--white);border:1px solid #ddd;font-family:'Tinos',serif;font-size:14px;color:#999;padding:14px 16px}
.subscribe-btn{position:absolute;left:659px;top:166px;width:178px;height:47px;background:var(--orange);color:var(--white);font-family:'Tinos',serif;font-size:21px;text-align:center;line-height:47px;text-transform:uppercase;letter-spacing:.5px}
.clients-title{position:absolute;left:0;top:305px;width:1200px;text-align:center;font-size:31px}
.client-row{position:absolute;left:160px;top:372px;width:880px;display:flex;justify-content:space-between;align-items:center}
.client-name{font-family:'Open Sans',sans-serif;font-weight:700;font-size:20px;color:#555;text-transform:uppercase;display:flex;align-items:center;gap:8px;white-space:nowrap}
.client-name i{display:block;width:14px;height:14px;border-radius:50%;background:#777}

/* footer */
.site-footer{position:absolute;left:0;top:2543px;width:1200px;height:269px;background:var(--black);color:var(--white)}
.footer-col{position:absolute;top:44px;text-align:center;font-size:13px;line-height:28px;color:#eee}
.footer-col svg{display:block;margin:0 auto 10px}
.social{position:absolute;left:547px;top:170px;display:flex;gap:10px}
.social span{width:28px;height:28px;border-radius:50%;background:var(--white)}
.copyright{position:absolute;left:0;top:226px;width:1200px;text-align:center;font-family:'Tinos',serif;font-size:12px;color:#999}
</style>
</head>
<body>

<header class="site-header">
  <div class="brand"><span class="brand-mark"></span><span class="brand-name">VistaLume</span></div>
  <nav class="main-nav">
    <a class="is-active" href="#">Home</a><a href="#">About Us</a><a href="#">Services</a><a href="#">Why Choose Us</a><a href="#">Contact Us</a><a href="#">Clients &amp; Partners</a><a href="#">Gallery</a>
  </nav>
</header>

<section class="hero" role="img" aria-label="Family watching a wall-mounted screen from a white sofa in a bright living room">
  <div class="hero-floor"></div>
</section>
<div class="hero-rule"></div>
<svg class="abs" style="left:578px;top:558px" width="44" height="20" viewBox="0 0 44 20"><path d="M0 0 H44 L22 20 Z" fill="var(--orange)"/></svg>
<div class="hero-caption"><h1><em>VistaLume</em> owns and maintains<br>a state of the art digital<br>signage network</h1></div>

<h2 class="section-title abs welcome-title">Welcome to VistaLume</h2>
<p class="serif-copy abs welcome-copy">We are the easiest access to conduct promotional activities in hospitals With exclusive and highly segmented target, We help advertisers to deliver his message precisely and to the point in a way that is unique and different The first and easiest access to the client, not make Our second priority to the hospital as we partner, but we also provide the best service facilities with the means of the promotion . Now, advertising not just only on the outside but also on speci area inside</p>
<div class="video-frame">
  <div class="video-still" role="img" aria-label="Video still of patients watching a screen in a waiting room"></div>
  <div class="video-bar">
    <svg class="abs" style="left:20px;top:8px" width="14" height="14" viewBox="0 0 14 14"><path d="M2 1 L13 7 L2 13 Z" fill="#fff"/></svg>
    <div class="video-progress"><span></span></div>
  </div>
</div>

<section class="services" role="img" aria-label="Blurred bright hospital corridor">
  <svg class="abs" style="left:570px;top:-1px" width="60" height="24" viewBox="0 0 60 24"><path d="M0 0 H60 L30 24 Z" fill="var(--white)"/></svg>
  <h2 class="section-title services-title">Services</h2>

  <div class="service-card is-active" style="left:150px;top:145px">
    <svg class="service-icon" viewBox="0 0 54 54"><circle cx="27" cy="27" r="26" fill="var(--orange)"/><rect x="16" y="19" width="22" height="15" rx="2" fill="none" stroke="#fff" stroke-width="3"/><path d="M23 37h8" stroke="#fff" stroke-width="3"/></svg>
    <h3>Digital Signage</h3><p>Lorem Ipsum is simply dummy text of the printing all of and typesetting industry.</p>
  </div>
  <div class="service-card" style="left:469px;top:145px">
    <svg class="service-icon" viewBox="0 0 54 54"><circle cx="27" cy="27" r="26" fill="var(--orange)"/><rect x="14" y="21" width="18" height="14" rx="2" fill="#fff"/><path d="M33 28l8-5v10z" fill="#fff"/></svg>
    <h3>Video Content Production</h3><p>Lorem Ipsum is simply dummy text of the printing all of and typesetting industry.</p>
  </div>
  <div class="service-card" style="left:790px;top:145px">
    <svg class="service-icon" viewBox="0 0 54 54"><circle cx="27" cy="27" r="26" fill="var(--orange)"/><path d="M27 15v24M15 27h24" stroke="#fff" stroke-width="6"/></svg>
    <h3>Hospital Branding</h3><p>Lorem Ipsum is simply dummy text of the printing all of and typesetting industry.</p>
  </div>
  <div class="service-card" style="left:150px;top:323px">
    <svg class="service-icon" viewBox="0 0 54 54"><circle cx="27" cy="27" r="26" fill="var(--orange)"/><rect x="16" y="17" width="22" height="21" rx="2" fill="none" stroke="#fff" stroke-width="3"/><path d="M16 24h22" stroke="#fff" stroke-width="3"/></svg>
    <h3>Event Management</h3><p>Lorem Ipsum is simply dummy text of the printing all of and typesetting industry.</p>
  </div>
  <div class="service-card" style="left:469px;top:323px">
    <svg class="service-icon" viewBox="0 0 54 54"><circle cx="27" cy="27" r="26" fill="var(--orange)"/><rect x="17" y="16" width="20" height="14" fill="none" stroke="#fff" stroke-width="3"/><path d="M27 30v9M21 39h12" stroke="#fff" stroke-width="3"/></svg>
    <h3>Seminar</h3><p>Lorem Ipsum is simply dummy text of the printing all of and typesetting industry.</p>
  </div>
  <div class="service-card" style="left:790px;top:323px">
    <svg class="service-icon" viewBox="0 0 54 54"><circle cx="27" cy="27" r="26" fill="var(--orange)"/><circle cx="27" cy="27" r="8" fill="none" stroke="#fff" stroke-width="5"/><circle cx="27" cy="27" r="13" fill="none" stroke="#fff" stroke-width="3" stroke-dasharray="4 4"/></svg>
    <h3>Queue System</h3><p>Lorem Ipsum is simply dummy text of the printing all of and typesetting industry.</p>
  </div>
  <div class="service-card" style="left:469px;top:502px">
    <svg class="service-icon" viewBox="0 0 54 54"><circle cx="27" cy="27" r="26" fill="var(--orange)"/><rect x="18" y="15" width="18" height="24" rx="2" fill="none" stroke="#fff" stroke-width="3"/><path d="M27 21v10M22 26h10" stroke="#fff" stroke-width="3"/></svg>
    <h3>Hospital Management</h3><p>Lorem Ipsum is simply dummy text of the printing all of and typesetting industry.</p>
  </div>
  <svg class="abs" style="left:570px;top:643px" width="60" height="24" viewBox="0 0 60 24"><path d="M0 24 H60 L30 0 Z" fill="var(--white)"/></svg>
</section>

<div class="why-photo" role="img" aria-label="Smiling man pointing a remote control at a screen"></div>
<h2 class="section-title abs why-title">Why Choose Us?</h2>
<p class="serif-copy abs why-copy">Lorem Ipsum is simply dummy text of the printing and typesetting industry. Lorem Ipsum has been the industry's standard dummy text ever since the 1500s, when an unknown printer took a galley of type and scrambled it to make a type specimen book. It has survived not only five centuries.</p>

<section class="newsletter">
  <svg class="abs" style="left:570px;top:-1px" width="60" height="24" viewBox="0 0 60 24"><path d="M0 0 H60 L30 24 Z" fill="var(--white)"/></svg>
  <h2 class="section-title newsletter-title">Get Our Newsletter</h2>
  <p class="serif-copy newsletter-sub">Get your Regular Email for Recieving the Update News and Events.</p>
  <div class="email-field">Enter Your Email...</div>
  <div class="subscribe-btn">Subscribe</div>
  <svg class="abs" style="left:136px;top:256px" width="928" height="8" viewBox="0 0 928 8">
    <defs><pattern id="zigzag-rule" width="8" height="8" patternUnits="userSpaceOnUse"><path d="M0 6 L4 2 L8 6" fill="none" stroke="#bbb" stroke-width="1.5"/></pattern></defs>
    <rect width="928" height="8" fill="url(#zigzag-rule)"/>
  </svg>
  <h2 class="section-title clients-title">Our Clients and Partners</h2>
  <div class="client-row">
    <span class="client-name">Ardent</span>
    <span class="client-name"><i></i>Kelvo</span>
    <span class="client-name"><i></i>Nuvari</span>
    <span class="client-name"><i></i>Solmet</span>
    <span class="client-name">Brisque</span>
    <span class="client-name">Halden Brew</span>
  </div>
</section>

<footer class="site-footer">
  <svg class="abs" style="left:0;top:-7px" width="1200" height="8" viewBox="0 0 1200 8">
    <defs><pattern id="footer-teeth" width="12" height="8" patternUnits="userSpaceOnUse"><path d="M0 8 L6 0 L12 8 Z" fill="var(--black)"/></pattern></defs>
    <rect width="1200" height="8" fill="url(#footer-teeth)"/>
  </svg>
  <div class="footer-col" style="left:200px;width:160px">
    <svg width="20" height="20" viewBox="0 0 20 20"><path d="M4 2l4 0 1 5-3 2c1 2 3 4 5 5l2-3 5 1v4c-8 1-15-6-14-14z" fill="#fff"/></svg>
    Phone: &nbsp;(021) 555-0142<br>Fax: &nbsp;&nbsp;&nbsp;&nbsp;(021) 555-0187
  </div>
  <div class="footer-col" style="left:430px;width:340px">
    <svg width="20" height="22" viewBox="0 0 20 22"><path d="M10 1a7 7 0 0 0-7 7c0 5 7 13 7 13s7-8 7-13a7 7 0 0 0-7-7z" fill="#fff"/><circle cx="10" cy="8" r="2.5" fill="var(--black)"/></svg>
    Graha Meridian Level 3, Suite 302<br>Jl. Kenanga Raya Kav. 75 , Jakarta Barat.
  </div>
  <div class="footer-col" style="left:823px;width:220px">
    <svg width="22" height="18" viewBox="0 0 22 18"><rect x="1" y="2" width="20" height="14" fill="#fff"/><path d="M1 2l10 8 10-8" fill="none" stroke="var(--black)" stroke-width="1.5"/></svg>
    info@vistalume.example.id
  </div>
  <div class="social"><span></span><span></span><span></span></div>
  <p class="copyright">Copyright © 2013 VistaLume. All Rights Reserved.</p>
</footer>

</body>
</html>
```